KESTREL REFRIGERATION Business Card design

We are looking for a business card design front and back. We would like our logo only on the front with all other details on the rear.
Rear should include name, email address and two phone numbers. Similar to the attachment.
Smart and bright.
Looking for a matt finish on all of the card but the logo to be gloss and slightly proud.

Contact Information for Business Card

Name - Gavin Holloway
Director
Phone - 0867302948
0417259083
email - gavin@kestrelrefrigeration.com.au
website - kestrelrefrigeration.com.au

Font styles to use
Serif

Requirements
Must have
• Colours from our logo. icons for phone, email etc.

```html
<!DOCTYPE html>
<html lang="en">
<head>
<meta charset="utf-8">
<title>Kestrel Refrigeration – Business Card</title>
<link href="https://fonts.googleapis.com/css2?family=Montserrat:wght@400;500;800&display=swap" rel="stylesheet">
<style>
  :root {
    --backdrop: #c9cacc;
    --brand-green: #168a16;
    --bright-green: #22b81e;
    --ink-green: #137a13;
    --card-white: #f6f6f4;
    --ink: #1d1d1d;
    --white: #ffffff;
  }
  * { box-sizing: border-box; margin: 0; padding: 0; }
  html, body {
    width: 1200px; height: 1150px; overflow: hidden;
    background: var(--backdrop);
    font-family: "Montserrat", Arial, sans-serif;
  }
  .canvas {
    width: 1200px; height: 1150px;
    display: flex; flex-direction: column; align-items: center; justify-content: center;
    gap: 50px;
  }
  .card {
    width: 840px; height: 480px;
    box-shadow: 0 6px 18px rgba(0,0,0,0.18);
    position: relative;
  }
  /* Front */
  .card-front {
    background: var(--brand-green);
    display: flex; align-items: center; justify-content: center;
  }
  .brand-name-front {
    color: var(--white);
    font-weight: 800;
    text-align: center;
    line-height: 1.05;
  }
  .brand-name-front .word-main { display: block; font-size: 96px; letter-spacing: 2px; }
  .brand-name-front .word-sub { display: block; font-size: 34px; letter-spacing: 3px; }
  /* Back */
  .card-back {
    background: var(--card-white);
    display: flex; align-items: center;
  }
  .back-brand {
    width: 370px;
    display: flex; justify-content: center;
    color: var(--bright-green);
    font-weight: 800;
    text-align: center;
    line-height: 1.1;
  }
  .back-brand .word-main { display: block; font-size: 48px; letter-spacing: 1px; }
  .back-brand .word-sub { display: block; font-size: 17px; letter-spacing: 1.5px; }
  .divider {
    width: 2px; height: 300px; background: var(--bright-green);
  }
  .details {
    flex: 1;
    padding: 0 50px 0 44px;
  }
  .person { text-align: right; margin-bottom: 34px; }
  .person-name {
    font-size: 34px; font-weight: 800; color: var(--ink-green); letter-spacing: 3px;
  }
  .person-role {
    font-size: 20px; font-weight: 400; color: var(--ink); letter-spacing: 1px;
  }
  .person-rule {
    display: inline-block; width: 64px; height: 2px; background: var(--bright-green); margin-top: 4px;
  }
  .contact-list { list-style: none; }
  .contact-item {
    display: flex; align-items: center; gap: 16px;
    margin-bottom: 14px;
    color: var(--ink);
  }
  .contact-item.phone { font-size: 24px; letter-spacing: 1px; }
  .contact-item.small { font-size: 15px; }
  .icon { width: 30px; height: 30px; flex: none; }
</style>
</head>
<body>
<main class="canvas">
  <section class="card card-front" aria-label="Card front">
    <div class="brand-name-front">
      <span class="word-main">KESTREL</span>
      <span class="word-sub">REFRIGERATION</span>
    </div>
  </section>

  <section class="card card-back" aria-label="Card back">
    <div class="back-brand">
      <div>
        <span class="word-main">KESTREL</span>
        <span class="word-sub">REFRIGERATION</span>
      </div>
    </div>
    <div class="divider"></div>
    <div class="details">
      <div class="person">
        <div class="person-name">Gavin Holloway</div>
        <div class="person-role">Director</div>
        <span class="person-rule"></span>
      </div>
      <ul class="contact-list">
        <li class="contact-item phone">
          <svg class="icon" viewBox="0 0 30 30" aria-hidden="true">
            <circle cx="15" cy="15" r="15" fill="var(--brand-green)"/>
            <path d="M10 8.5c1-.6 1.8-.3 2.3.6l1.2 2.2c.4.8.2 1.5-.5 2l-.8.6c.7 1.7 2 3 3.7 3.8l.6-.8c.5-.7 1.2-.9 2-.5l2.2 1.2c.9.5 1.2 1.3.6 2.3-.8 1.3-2.2 1.9-3.7 1.4-4.1-1.3-7.2-4.4-8.5-8.5-.5-1.5.1-2.9 1.4-3.7z" fill="var(--white)"/>
          </svg>
          <span>0867302948</span>
        </li>
        <li class="contact-item phone">
          <svg class="icon" viewBox="0 0 30 30" aria-hidden="true">
            <circle cx="15" cy="15" r="15" fill="var(--brand-green)"/>
            <path d="M10 8.5c1-.6 1.8-.3 2.3.6l1.2 2.2c.4.8.2 1.5-.5 2l-.8.6c.7 1.7 2 3 3.7 3.8l.6-.8c.5-.7 1.2-.9 2-.5l2.2 1.2c.9.5 1.2 1.3.6 2.3-.8 1.3-2.2 1.9-3.7 1.4-4.1-1.3-7.2-4.4-8.5-8.5-.5-1.5.1-2.9 1.4-3.7z" fill="var(--white)"/>
          </svg>
          <span>0417259083</span>
        </li>
        <li class="contact-item small">
          <svg class="icon" viewBox="0 0 30 30" aria-hidden="true">
            <circle cx="15" cy="15" r="15" fill="var(--brand-green)"/>
            <g fill="none" stroke="var(--white)" stroke-width="1.4">
              <circle cx="15" cy="15" r="7.5"/>
              <ellipse cx="15" cy="15" rx="3.2" ry="7.5"/>
              <line x1="7.5" y1="15" x2="22.5" y2="15"/>
              <line x1="8.5" y1="11.3" x2="21.5" y2="11.3"/>
              <line x1="8.5" y1="18.7" x2="21.5" y2="18.7"/>
            </g>
          </svg>
          <span>www.kestrelrefrigeration.com.au</span>
        </li>
        <li class="contact-item small">
          <svg class="icon" viewBox="0 0 30 30" aria-hidden="true">
            <circle cx="15" cy="15" r="15" fill="var(--brand-green)"/>
            <rect x="8" y="10" width="14" height="10" rx="1" fill="var(--white)"/>
            <path d="M8.5 10.6 15 15.6l6.5-5" fill="none" stroke="var(--brand-green)" stroke-width="1.3"/>
          </svg>
          <span>gavin@kestrelrefrigeration.com.au</span>
        </li>
      </ul>
    </div>
  </section>
</main>
</body>
</html>
```